Men's Ministry Vellmoor Church "Note to Clergy"

We need to update brochure line-up to the 21st Century. This piece will explain the value that a men's ministry affords a local parish. A majority of priests (male and female) do not know what the Fellowship of St. Corwin can do to help them lay a solid foundation to grow, become more diversified, and present a positive picture for the local community

Under Must Not or avoid, please do not put the Fellowship logo on the Front Panel, back shield reduce keep low key it. We need a 21st Century look that will appeal to Millennials, Gen-Xers, younger generation. Shield was created in 1883, it is about time we changed it.

Target Market(s)

Male and female clergy in the Harrowdale Vellmoor Church

Industry/Entity Type

Non-Profit

Font styles to use
Serif

Requirements
Must have
• Slogan "Set Your Corwin Free"
• Snappy enough to invite people to pick -up
Nice to have
• Want to keep Fellowship of St. Corwin Logo on back panel, low keyed with address, web page and phone
Should not have
• political issues or political correctness

```html
<!DOCTYPE html>
<html lang="en">
<head>
<meta charset="utf-8">
<title>Set Your Corwin Free — Note to Clergy</title>
<link rel="stylesheet" href="https://fonts.googleapis.com/css2?family=Oswald:wght@400;600;700&family=Lato:wght@400;700&family=Lobster&display=swap">
<style>
  :root {
    --red: #e3141c;
    --purple: #4a22a6;
    --violet: #6a2fd0;
    --ink: #1f1f24;
    --charcoal: #333338;
    --paper: #ffffff;
    --stage: #d9d9dc;
    --lavender: #e6e1f4;
  }
  * { box-sizing: border-box; margin: 0; padding: 0; }
  html, body { width: 1200px; height: 1200px; overflow: hidden; background: var(--stage); }
  .brochure {
    position: absolute; left: 30px; top: 220px; width: 1140px; height: 760px;
    background: var(--paper); box-shadow: 0 10px 30px rgba(0,0,0,.18); overflow: hidden;
  }
  .panel { position: absolute; top: 0; width: 380px; height: 760px; overflow: hidden; }
  .panel--inside { left: 0; }
  .panel--back { left: 380px; border-left: 1px solid #eee; border-right: 1px solid #eee; }
  .panel--front { left: 760px; }
  .bands { position: absolute; inset: 0; pointer-events: none; }

  /* Inside flap */
  .photo-prayer {
    position: absolute; left: 0; top: 0; width: 380px; height: 260px;
    background: linear-gradient(135deg, #f3f1ee 0%, #c9b8a8 35%, #6b4a38 60%, #e8e4e0 100%);
    clip-path: polygon(0 0, 100% 0, 100% 92%, 0 74%);
  }
  .haze {
    position: absolute; left: 0; top: 240px; width: 380px; height: 160px;
    background: linear-gradient(180deg, var(--lavender), rgba(255,255,255,0));
  }
  .fit-heading {
    position: absolute; left: 30px; top: 330px;
    font: 700 22px/1 "Lato", sans-serif; color: var(--purple);
  }
  .fit-list {
    position: absolute; left: 30px; top: 366px; width: 330px; list-style: none;
    font: 700 13px/18px "Lato", sans-serif; color: var(--ink);
  }
  .fit-list li { position: relative; padding-left: 16px; }
  .fit-list li::before {
    content: ""; position: absolute; left: 2px; top: 6px; width: 6px; height: 6px;
    border-radius: 50%; background: var(--purple);
  }
  .web-link { font: 700 18px/1 "Lato", sans-serif; color: var(--red); position: absolute; }
  .panel--inside .web-link { left: 30px; top: 690px; }

  /* Back panel */
  .org-mark { position: absolute; left: 0; width: 380px; top: 60px; text-align: center; }
  .org-mark__dot { display: block; margin: 0 auto 12px; width: 26px; height: 26px; border-radius: 50%; background: var(--red); }
  .org-mark__name { font: 700 16px/1.2 "Lato", sans-serif; color: var(--purple); }
  .contact {
    position: absolute; left: 0; top: 170px; width: 380px; text-align: center;
    font: 400 12.5px/17px "Lato", sans-serif; color: var(--ink);
  }
  .photo-hands {
    position: absolute; left: 45px; top: 315px; width: 290px; height: 290px; border-radius: 50%;
    border: 10px solid var(--red); outline: 6px solid #fff;
    background: radial-gradient(circle at 40% 45%, #f6d9c1 0%, #d6a07a 30%, #8c9a3a 60%, #5a2a2a 100%);
  }
  .panel--back .web-link { left: 0; width: 380px; text-align: center; top: 650px; }

  /* Front panel */
  .front-bg {
    position: absolute; inset: 0;
    background: linear-gradient(180deg, #f4f2fb 0%, #ffffff 30%, #f1dff0 45%, #e5b8a0 65%, #c55a2a 85%, #4a1a24 100%);
  }
  .photo-cross {
    position: absolute; left: 60px; top: 360px; width: 280px; height: 370px;
    background: radial-gradient(ellipse at 50% 90%, #f7a43a 0%, #d2612a 35%, rgba(90,30,40,.85) 75%, rgba(90,30,40,0) 100%);
  }
  .slogan { position: absolute; left: 0; width: 380px; top: 40px; text-align: center; font-family: "Oswald", sans-serif; text-transform: uppercase; }
  .slogan__lead { display: block; font-weight: 700; font-size: 68px; line-height: 1; color: var(--red); }
  .slogan__name { display: block; font-weight: 600; font-size: 50px; line-height: 1.05; color: var(--charcoal); }
  .clergy-note {
    position: absolute; left: 50px; top: 200px; width: 280px; padding: 12px 10px 10px;
    background: var(--violet); color: #fff; text-align: center;
  }
  .clergy-note__greeting { font: 400 18px/1.2 "Lobster", cursive; }
  .clergy-note__body { font: 400 17px/1.2 "Oswald", sans-serif; margin-top: 6px; }
  .clergy-note__web { font: 400 10px/1 "Lato", sans-serif; margin-top: 6px; }
  .tagline { position: absolute; left: 0; width: 380px; top: 322px; text-align: center; font: 400 17px/1 "Lobster", cursive; color: var(--red); }
</style>
</head>
<body>
<main class="brochure">

  <section class="panel panel--inside">
    <div class="photo-prayer" role="img" aria-label="Photo of a family with eyes closed, hands folded in prayer"></div>
    <div class="haze"></div>
    <h2 class="fit-heading">Is It For Me?</h2>
    <ul class="fit-list">
      <li>Feeling out numbered?</li>
      <li>Annual pledges going down asked to give more &amp; more</li>
      <li>Children, EYC, numbers disappearing going away</li>
      <li>Doing grounds maintenance by yourself</li>
      <li>Diocesan pledges requirements going up</li>
      <li>No Bible study classes</li>
      <li>Not being spiritual enriching</li>
      <li>Wayfarer, Kindle, Road Retreat are a thing of the past</li>
      <li>When was the last time you were on a retreat with other men?</li>
      <li>Do you feel your voice is not being heard</li>
      <li>Seeking ways to define your spiritual journey</li>
      <li>Who is Jesus Christ?</li>
      <li>How do we pray?</li>
      <li>How do we comfort others?</li>
    </ul>
    <p class="web-link">www.fellowshipcorwin.org</p>
  </section>

  <section class="panel panel--back">
    <div class="org-mark">
      <span class="org-mark__dot"></span>
      <p class="org-mark__name">Fellowship of St. Corwin</p>
    </div>
    <address class="contact" style="font-style:normal">
      P.O. Box 418, Millbrook, OH 44021<br>
      www.fellowshipcorwin.org<br>
      Phone: 555-318-0427<br>
      E-mail: hello@fellowshipcorwin.org<br>
      Visit: http://www.fellowshipcorwin.org
    </address>
    <div class="photo-hands" role="img" aria-label="Photo of folded hands resting on an open Bible"></div>
    <p class="web-link">www.fellowshipcorwin.org</p>
  </section>

  <section class="panel panel--front">
    <div class="front-bg"></div>
    <div class="photo-cross" role="img" aria-label="Silhouette of a figure carrying a cross against a sunset sky"></div>
    <h1 class="slogan"><span class="slogan__lead">Set Your</span><span class="slogan__name">Corwin Free</span></h1>
    <div class="clergy-note">
      <p class="clergy-note__greeting">Dear Clergy,</p>
      <p class="clergy-note__body">Embrace men's ministries with the Fellowship of Saint Corwin</p>
      <p class="clergy-note__web">www.fellowshipcorwin.org</p>
    </div>
    <p class="tagline">It's A No-brainer &nbsp;"Come and See!"</p>
  </section>

  <svg class="bands" width="1140" height="760" viewBox="0 0 1140 760">
    <polygon points="0,190 380,238 380,252 0,204" fill="var(--red)"/>
    <polygon points="380,238 760,330 760,344 380,252" fill="var(--purple)"/>
    <rect x="0" y="732" width="380" height="28" fill="var(--red)"/>
    <rect x="380" y="732" width="380" height="28" fill="var(--purple)"/>
    <rect x="760" y="732" width="380" height="28" fill="var(--red)"/>
    <rect x="760" y="726" width="380" height="4" fill="#fff"/>
  </svg>
</main>
</body>
</html>
```